Brightfield Ledger blog

We need two websites: both are already online, using Drupal.
I would prefer to use Drupal for both, so if you know nothing about Drupal, or wld prefer to use Wordpress please don't submit a proposal.
One website will be a blog. The domain is brightfieldledger.com.
For this site, we need to be able to post blogs; take comments; invite members; perhaps send out a weekly newsletter; and perhaps introduce weekly interactive elements e.g. a poll.
The other website is to house a new company. The domain is tkdpower.com.
This would also be very simple, allowing for administrator and third party posts and blogs, and interactive elements such as forums.
Neither project is ambitious; the priority is a simple to use, attractive, professional looking shop window.
Updates

i havent had much interest in this web design and coding project; am therefore happy to make brief the project easier/ better value - i need coding, and that is included in the fee. but am happy to limit this to home page for one website; we can negotiate a higher fee for an additional home page for another website; and i am happy if you work in wordpress or other; i prefer drupal simply because that is the template we are using at present. in addition i am happy to guarantee the project for the right designer, if thats a priority

Reason: project extended just to give us time to make a decision on Monday/ Tuesday !

Industry/Entity Type

Online

Coding

Coded - Design and coding required

```html
<!DOCTYPE html>
<html lang="en">
<head>
<meta charset="utf-8">
<title>Brightfield Ledger Blog</title>
<link href="https://fonts.googleapis.com/css2?family=Lato:wght@400;700&family=Open+Sans:wght@400;600&family=Oswald:wght@400;500&display=swap" rel="stylesheet">
<style>
:root{
  --orange:#e0691a;
  --orange-dark:#d2600f;
  --text:#444;
  --muted:#777;
  --line:#e4e4e4;
  --panel:#f7f7f7;
  --white:#fff;
  --blue:#3a8fd6;
}
*{box-sizing:border-box;margin:0;padding:0}
html,body{width:1200px;height:2329px;overflow:hidden;background:var(--white)}
body{position:relative;font-family:"Open Sans",sans-serif;color:var(--text)}
.abs{position:absolute}
/* header */
.brand{left:172px;top:30px;display:flex;align-items:center;gap:16px}
.brand-mark{width:46px;height:46px;background:var(--orange)}
.brand-name{font-family:"Lato",sans-serif;font-size:23px;color:#555;letter-spacing:.5px}
.brand-tag{font-family:"Lato",sans-serif;font-size:12px;color:#555;margin-top:4px}
.nav{right:171px;top:45px;display:flex;font-family:"Lato",sans-serif;font-size:14px}
.nav a{color:#555;text-decoration:none;padding:0 20px;border-left:1px solid #ddd;line-height:18px}
.nav a:first-child{border-left:0;color:var(--orange)}
.nav a:last-child{padding-right:0}
/* hero */
.hero{left:0;top:113px;width:1200px;height:517px;background:linear-gradient(180deg,#9fb3a4 0%,#b9c7b4 35%,#6f9049 62%,#4d7a2a 100%)}
.hero-arrow{top:233px;width:32px;height:32px;border-radius:50%;background:rgba(60,60,60,.6);display:flex;align-items:center;justify-content:center}
.hero-caption{left:172px;top:182px;width:427px;height:155px;background:rgba(70,70,70,.6);padding:14px 20px;color:var(--white)}
.hero-caption h1{font-family:"Oswald",sans-serif;font-weight:500;font-size:40px;line-height:48px}
.hero-caption p{font-family:"Lato",sans-serif;font-weight:700;font-size:15px;line-height:25px;margin-top:6px}
.welcome{left:172px;top:565px;width:857px;height:112px;background:var(--white);text-align:center;padding-top:20px}
.welcome h2{font-family:"Lato",sans-serif;font-weight:700;font-size:31px;color:#444}
.welcome p{font-size:12px;line-height:19px;color:#555;margin:14px auto 0;width:770px}
/* posts */
.post{left:172px;width:559px}
.post-photo{width:559px;height:241px;border:1px solid #ddd;padding:5px;box-shadow:0 1px 3px rgba(0,0,0,.12)}
.post-photo div{width:100%;height:100%}
.post-title{font-family:"Lato",sans-serif;font-size:21px;color:#444;font-weight:400;margin-top:22px}
.post-meta{display:flex;align-items:center;font-size:11px;color:#333;margin-top:12px;gap:12px}
.stars{display:flex;gap:1px;padding-right:12px;border-right:1px solid #ddd}
.post-date{margin-left:12px}
.post-excerpt{font-size:11px;line-height:19px;color:#666;margin-top:12px}
.read-more{display:block;font-size:11px;color:var(--orange);margin-top:14px;text-decoration:none}
/* sidebar */
.side{left:762px;width:267px}
.poll{top:723px;height:271px;background:var(--panel);border:1px solid #eee}
.poll-photo{height:87px;background:linear-gradient(135deg,#3d3d3d,#6e8f3c 70%,#3d3d3d);display:flex;align-items:center;justify-content:center;color:var(--white);font-family:"Lato",sans-serif;font-weight:700;font-size:21px;text-align:center;line-height:26px}
.poll ul{list-style:none;padding:18px 20px 0}
.poll li{font-size:12px;color:#555;display:flex;align-items:center;gap:12px;height:26px}
.box{width:12px;height:12px;border:1px solid #bbb;background:var(--white)}
.btn-vote{margin:14px 0 0 20px;display:inline-block;background:var(--orange);color:var(--white);font-size:14px;padding:4px 14px;border-radius:2px}
.login{top:1009px;height:202px;background:var(--panel);border:1px solid #eee;padding:17px 27px 0}
.login h3{text-align:center;font-family:"Lato",sans-serif;font-weight:700;font-size:21px;color:var(--orange)}
.field{height:28px;border:1px solid #ccc;border-radius:14px;background:var(--white);margin-top:12px;font-size:10px;color:#999;padding:7px 0 0 30px}
.field:first-of-type{margin-top:14px}
.login-row{display:flex;justify-content:space-between;align-items:center;margin-top:10px;font-size:9px;color:#999}
.btn-login{background:var(--blue);color:var(--white);font-size:15px;border-radius:15px;padding:5px 0;width:104px;text-align:center}
.section-label{font-family:"Lato",sans-serif;font-size:15px;color:#333}
.recent{display:flex;gap:18px;border-bottom:1px solid var(--line);padding-bottom:14px}
.recent-photo{width:82px;height:82px;flex:none}
.recent h4{font-family:"Lato",sans-serif;font-weight:400;font-size:12px;color:#666}
.recent .by{font-size:10px;color:var(--orange);margin-top:8px}
.recent p{font-size:10px;line-height:19px;color:#888;margin-top:6px}
.tweets{top:1650px;height:275px;background:var(--panel);border:1px solid #eee}
.tweets-head{display:flex;justify-content:space-between;align-items:center;padding:15px 17px 13px;border-bottom:1px solid var(--line)}
.tweets-head span{font-family:"Lato",sans-serif;font-size:16px;color:var(--orange)}
.btn-follow{font-size:9px;border:1px solid #ccc;background:#eee;padding:2px 8px;border-radius:2px;color:#333}
.tweet{display:flex;gap:16px;padding:15px 17px;border-bottom:1px solid var(--line)}
.tweet:last-child{border-bottom:0}
.avatar{width:60px;height:74px;background:linear-gradient(180deg,#cfcfcf,#9a8f88);flex:none}
.tweet b{font-family:"Lato",sans-serif;font-weight:400;font-size:15px;color:#444;display:block}
.tweet i{font-style:normal;font-size:11px;color:#444;display:block;margin-top:4px}
.tweet p{font-size:11px;line-height:18px;color:#444;margin-top:2px}
.signup{top:1950px;height:194px;background:var(--orange);color:var(--white);text-align:center;padding-top:12px}
.signup h3{font-family:"Oswald",sans-serif;font-weight:400;font-size:22px}
.signup p{font-family:"Oswald",sans-serif;font-size:18px;margin-top:2px;opacity:.95}
.signup-field{width:200px;height:36px;border:1px solid rgba(255,255,255,.85);border-radius:3px;margin:14px auto 0;font-size:12px;line-height:34px}
.signup-field+.signup-field{margin-top:13px}
/* footer */
.footer{left:0;top:2189px;width:1200px;height:140px;background:var(--orange-dark);color:var(--white);text-align:center;padding-top:27px}
.footer-nav{font-size:12px}
.footer-nav span{margin:0 6px}
.copyright{font-size:12px;margin-top:14px}
.social{display:flex;justify-content:center;gap:6px;margin-top:16px}
.social span{width:28px;height:28px;border:1px solid rgba(255,255,255,.9);border-radius:50%}
</style>
</head>
<body>

<header>
  <div class="abs brand">
    <div class="brand-mark"></div>
    <div>
      <div class="brand-name">BRIGHTFIELD LEDGER BLOG</div>
      <div class="brand-tag">Intelligent comment, from Martin Hale and Paul Derwent</div>
    </div>
  </div>
  <nav class="abs nav"><a>HOME</a><a>ABOUT US</a><a>NEWS</a><a>BLOG</a><a>LOGIN</a></nav>
</header>

<section class="abs hero" role="img" aria-label="Photo of wind turbines over a green field under a cloudy sky"></section>
<div class="abs hero-arrow" style="left:33px;top:346px"><svg width="12" height="12" viewBox="0 0 12 12"><path d="M8 1 3 6l5 5" fill="none" stroke="#fff" stroke-width="2"/></svg></div>
<div class="abs hero-arrow" style="left:1130px;top:346px"><svg width="12" height="12" viewBox="0 0 12 12"><path d="M4 1l5 5-5 5" fill="none" stroke="#fff" stroke-width="2"/></svg></div>
<div class="abs hero-caption">
  <h1>Brightfield Ledger Blog.</h1>
  <p>Welcome to the Brightfield Ledger Blog. You will find here blogs on the worlds of energy, carbon and climate change, across markets,</p>
</div>

<section class="abs welcome">
  <h2>Welcome To Brightfield Ledger</h2>
  <p>Welcome to the Brightfield Ledger Blog. You will find here blogs on the worlds of energy, carbon and climate change, across markets, business, policy and science, posted by Martin Hale and Paul Derwent, of Norwell Capital and TKD Power.</p>
</section>

<article class="abs post" style="top:723px">
  <div class="post-photo"><div role="img" aria-label="Businesswoman pointing at a crumbling dollar sign" style="background:linear-gradient(90deg,#e9ebee,#7d8fb0 30%,#e9ebee 55%,#c9b89a 75%,#eeeeee)"></div></div>
  <h3 class="post-title">Paradox of European power prices…</h3>
  <div class="post-meta">
    <span class="stars"><svg width="56" height="10" viewBox="0 0 56 10"><g fill="#e8a32b"><path id="s" d="M5 0l1.5 3.3 3.5.4-2.6 2.4.7 3.5L5 7.8 1.9 9.6l.7-3.5L0 3.7l3.5-.4z"/><use href="#s" x="11"/><use href="#s" x="22"/></g><g fill="none" stroke="#bbb" stroke-width=".8"><use href="#s" x="33"/><use href="#s" x="44"/></g></svg></span>
    <svg width="12" height="12" viewBox="0 0 12 12"><path d="M1 5h2v6H1zM4 11V5l3-4c1 0 1.5.6 1.2 2L8 4.5h3l-.8 6.5z" fill="none" stroke="#e0691a"/></svg>
    <span>Submitted by Martinhale on</span><span class="post-date">Wed, 11/19/2014 - 11:53</span>
  </div>
  <p class="post-excerpt">Power prices is not an easy topic to talk about. First and foremost, there are lots of different power prices from baseload to peak, from wholesale to retail, from heavy industry to commercial prices. And each country across Europe has different prices and then there are renewables pushing up the power prices, or so they say. Then we have the European Union with their goal of making energy "affordable, competitively priced, environmentally sustainable and secure for everybody." And how are they doing this.</p>
  <a class="read-more">Read more +</a>
</article>

<article class="abs post" style="top:1209px">
  <div class="post-photo"><div role="img" aria-label="Cooling towers of a nuclear plant at sunset" style="background:linear-gradient(180deg,#3d4a5c,#8ca0b6 35%,#e9a35b 70%,#c0542a)"></div></div>
  <h3 class="post-title">The Nuclear Renaissance?</h3>
  <div class="post-meta">
    <span class="stars"><svg width="56" height="10" viewBox="0 0 56 10"><g fill="#e8a32b"><use href="#s"/><use href="#s" x="11"/><use href="#s" x="22"/></g><g fill="none" stroke="#bbb" stroke-width=".8"><use href="#s" x="33"/><use href="#s" x="44"/></g></svg></span>
    <svg width="12" height="12" viewBox="0 0 12 12"><path d="M1 5h2v6H1zM4 11V5l3-4c1 0 1.5.6 1.2 2L8 4.5h3l-.8 6.5z" fill="none" stroke="#e0691a"/></svg>
    <span>Submitted by Martinhale on</span><span class="post-date">Wed, 11/19/2014 - 11:53</span>
  </div>
  <p class="post-excerpt">Power prices is not an easy topic to talk about. First and foremost, there are lots of different power prices from baseload to peak, from wholesale to retail, from heavy industry to commercial prices. And each country across Europe has different prices and then there are renewables pushing up the power prices, or so they say. Then we have the European Union with their goal of making energy "affordable, competitively priced, environmentally sustainable and secure for everybody." And how are they doing this.</p>
  <a class="read-more">Read more +</a>
</article>

<article class="abs post" style="top:1694px">
  <div class="post-photo"><div role="img" aria-label="Oil pump jack silhouetted against an orange sunset" style="background:linear-gradient(180deg,#c46a1e,#f2a432 60%,#e0731c 80%,#3a1c0c)"></div></div>
  <h3 class="post-title">Paradox of European power prices…</h3>
  <div class="post-meta">
    <span class="stars"><svg width="56" height="10" viewBox="0 0 56 10"><g fill="#e8a32b"><use href="#s"/><use href="#s" x="11"/><use href="#s" x="22"/></g><g fill="none" stroke="#bbb" stroke-width=".8"><use href="#s" x="33"/><use href="#s" x="44"/></g></svg></span>
    <svg width="12" height="12" viewBox="0 0 12 12"><path d="M1 5h2v6H1zM4 11V5l3-4c1 0 1.5.6 1.2 2L8 4.5h3l-.8 6.5z" fill="none" stroke="#e0691a"/></svg>
    <span>Submitted by Martinhale on</span><span class="post-date">Wed, 11/19/2014 - 11:53</span>
  </div>
  <p class="post-excerpt">Power prices is not an easy topic to talk about. First and foremost, there are lots of different power prices from baseload to peak, from wholesale to retail, from heavy industry to commercial prices. And each country across Europe has different prices and then there are renewables pushing up the power prices, or so they say. Then we have the European Union with their goal of making energy "affordable, competitively priced, environmentally sustainable and secure for everybody." And how are they doing this.</p>
  <a class="read-more">Read more +</a>
</article>

<aside>
  <section class="abs side poll">
    <div class="poll-photo" role="img" aria-label="Keyboard with a green poll key">TODAY'S<br>POLL</div>
    <ul>
      <li><svg class="box" viewBox="0 0 12 12"><path d="M2.5 6l2.5 2.5 4.5-5" fill="none" stroke="#555" stroke-width="1.4"/></svg>Sed ut perspiciatis unde</li>
      <li><span class="box"></span>Lorem ipsum dolor sit amet</li>
      <li><span class="box"></span>Ut enim ad minim</li>
      <li><span class="box"></span>Nemo enim ipsam voluptatem</li>
    </ul>
    <span class="btn-vote">Vote</span>
  </section>

  <section class="abs side login">
    <h3>USER LOGIN</h3>
    <div class="field">Username</div>
    <div class="field">Password</div>
    <div class="login-row"><span>☑ Remember Me</span><span class="btn-login">LOG IN</span></div>
  </section>

  <div class="abs side section-label" style="top:1228px">RECENT BLOG</div>
  <div class="abs side recent" style="top:1281px">
    <div class="recent-photo" role="img" aria-label="Man reading at a desk" style="background:linear-gradient(135deg,#dfe4ea,#4d5f7a)"></div>
    <div><h4>Paradox of European power</h4><div class="by">19 November, Martin Hale</div><p>The European Commission's recent decision to allow</p></div>
  </div>
  <div class="abs side recent" style="top:1402px">
    <div class="recent-photo" role="img" aria-label="Oil pump against a blue sky" style="background:linear-gradient(180deg,#a8c4dc,#3e6a93)"></div>
    <div><h4>Paradox of European power</h4><div class="by">19 November, Martin Hale</div><p>The European Commission's recent decision to allow</p></div>
  </div>
  <div class="abs side recent" style="top:1529px;border-bottom:0">
    <div class="recent-photo" role="img" aria-label="Construction cranes over a building site" style="background:linear-gradient(180deg,#8fb2d6,#c9a36f 70%,#6c5a45)"></div>
    <div><h4>Paradox of European power</h4><div class="by">19 November, Martin Hale</div><p>The European Commission's recent decision to allow</p></div>
  </div>

  <section class="abs side tweets">
    <div class="tweets-head"><span>Tweets Feed</span><span class="btn-follow">Follow</span></div>
    <div class="tweet">
      <div class="avatar" role="img" aria-label="Profile portrait"></div>
      <div><b>Energy and Climate</b><i>@paulderwent</i><p>China off course for 2020 carbon emissions target</p></div>
    </div>
    <div class="tweet">
      <div class="avatar" role="img" aria-label="Profile portrait"></div>
      <div><b>Energy and Climate</b><i>@paulderwent</i><p>China off course for 2020 carbon emissions target</p></div>
    </div>
  </section>

  <section class="abs side signup">
    <h3>FREE SIGNUP</h3>
    <p>Please click here to free signup.</p>
    <div class="signup-field">E - Mail</div>
    <div class="signup-field">SIGNUP</div>
  </section>
</aside>

<footer class="abs footer">
  <div class="footer-nav">Home<span>/</span>About Us<span>/</span>Blogs<span>/</span>News<span>/</span>User login<span>/</span>Get in Touch</div>
  <div class="copyright">©2013 - 2014&nbsp; Brightfield Ledger Blog. All Rights Reserved.</div>
  <div class="social"><span></span><span></span><span></span><span></span><span></span></div>
</footer>

</body>
</html>
```